Flyer for IT Support Company

We need a 1 sided A5 flyer to promote our services and support packages to local businesses, I have attached the sort of content and layout we are looking for but happy for you to be creative with backgrounds and colors. It needs to look modern and professional but catch the eye ;-)
The strap-line on the logo needs to be changed to to 'Your Local IT Company'

It Company

```html
<!DOCTYPE html>
<html lang="en">
<head>
<meta charset="utf-8">
<title>Corvanta – Affordable IT Support Packages</title>
<link rel="stylesheet" href="https://fonts.googleapis.com/css2?family=Arimo:wght@400;700&family=Archivo+Black&display=swap">
<style>
  :root {
    --green: #8cc63f;
    --green-dark: #5f9a22;
    --green-text: #4f8a1c;
    --magenta: #c2187a;
    --magenta-dark: #8e1159;
    --navy: #1d2550;
    --navy-light: #27306a;
    --cell-blue: #2f6fc0;
    --cell-blue-light: #4b8fdb;
    --grey-text: #444;
    --panel: #f4f4f4;
    --white: #ffffff;
  }
  * { box-sizing: border-box; margin: 0; padding: 0; }
  html, body { width: 959px; height: 1200px; overflow: hidden; background: var(--white); }
  body { position: relative; font-family: "Arimo", Arial, sans-serif; }

  .flyer {
    position: absolute; left: 68px; top: 50px; width: 822px; height: 1062px;
    background: linear-gradient(180deg, var(--green) 0%, #9fd055 40%, #e9ecea 58%, #f2f2f2 100%);
    overflow: hidden;
  }
  .swoosh { position: absolute; left: 0; top: 0; width: 822px; height: 1062px; }

  .hero-photo {
    position: absolute; left: 0; top: 0; width: 402px; height: 540px;
    background: linear-gradient(160deg, #5a5f66 0%, #2c3037 45%, #6f7d92 75%, #3b4a63 100%);
  }

  .brand {
    position: absolute; left: 420px; top: 2px; width: 382px; height: 118px;
    background: linear-gradient(180deg, #ffffff 0%, #e7e7e7 100%);
    border-radius: 6px; box-shadow: 0 4px 10px rgba(0,0,0,.25);
    text-align: center;
  }
  .brand-name {
    display: flex; align-items: center; justify-content: center; gap: 12px;
    margin-top: 14px; font-family: "Arimo", Arial, sans-serif; font-weight: 700;
    font-size: 62px; line-height: 64px; color: var(--green); letter-spacing: -1px;
  }
  .brand-dot { width: 44px; height: 44px; border-radius: 50%; background: var(--green); }
  .brand-strap {
    font-weight: 700; font-size: 14px; letter-spacing: 3px; color: var(--green);
    margin-top: 10px;
  }

  .circle {
    position: absolute; border-radius: 50%; border: 6px solid #f0f0f0;
    box-shadow: 0 3px 10px rgba(0,0,0,.3); overflow: hidden;
  }
  .circle-product { left: 410px; top: 325px; width: 190px; height: 190px; background: radial-gradient(circle, #ffffff 0%, #dcdcdc 100%); }
  .circle-person { left: 582px; top: 215px; width: 310px; height: 310px; background: radial-gradient(circle at 55% 40%, #d8dde4 0%, #9fb7d6 55%, #e8e8e8 100%); }
  .circle .fill { width: 100%; height: 100%; }

  .panel {
    position: absolute; left: 32px; top: 540px; width: 760px; height: 480px;
    background: var(--panel);
  }

  .packages {
    position: absolute; left: 84px; top: 572px; width: 295px; table-layout: fixed;
    border-collapse: separate; border-spacing: 2px 0; font-size: 8.5px; color: var(--white);
  }
  .packages col.col-label { width: 148px; }
  .packages col.col-plan { width: 34px; }
  .packages th { color: var(--green-text); font-size: 7.5px; font-weight: 700; height: 20px; text-align: center; white-space: nowrap; }
  .packages th.title { text-align: left; font-size: 10px; }
  .packages td { height: 16px; text-align: center; background: var(--cell-blue); border-bottom: 1px solid var(--cell-blue-light); white-space: nowrap; overflow: hidden; }
  .packages td.label { text-align: left; padding-left: 7px; background: var(--navy); border-bottom: 1px solid var(--navy-light); }
  .packages tr.price td.label { background: var(--green-dark); }
  .packages tr.price td { background: var(--navy); }
  .packages tr.section td {
    background: var(--magenta); color: var(--white); font-weight: 700; height: 14px; border: 0;
  }
  .packages .small { font-size: 6px; }
  .tick {
    display: inline-block; width: 4px; height: 7px; border: solid var(--white);
    border-width: 0 1.6px 1.6px 0; transform: rotate(45deg); margin-bottom: 2px;
  }

  .headline { position: absolute; left: 415px; top: 650px; color: var(--green-text); }
  .headline-main { font-family: "Archivo Black", Arial, sans-serif; font-size: 45px; line-height: 46px; }
  .headline-sub { font-family: "Archivo Black", Arial, sans-serif; font-size: 25px; line-height: 30px; }
  .headline-sub span { font-family: "Arimo", Arial, sans-serif; font-weight: 400; }
  .headline-tag { font-size: 14px; color: var(--grey-text); margin-top: 1px; }

  .offer-band {
    position: absolute; left: 388px; top: 765px; width: 382px; height: 62px;
    background: linear-gradient(90deg, var(--magenta-dark), var(--magenta) 40%, var(--magenta-dark));
    color: var(--white); display: flex; align-items: center;
  }
  .offer-left { width: 136px; text-align: center; font-size: 16px; line-height: 19px; border-right: 1px solid rgba(255,255,255,.7); padding: 2px 0; margin-left: 4px; }
  .offer-right { flex: 1; text-align: center; font-size: 15.5px; line-height: 19px; }
  .offer-band b { font-weight: 700; }

  .features { position: absolute; left: 402px; top: 850px; width: 380px; height: 90px; }
  .feature { position: absolute; display: flex; align-items: center; gap: 6px; font-size: 15px; line-height: 16px; color: var(--grey-text); }
  .feature b { color: var(--magenta); font-weight: 700; }
  .feature svg { flex: none; }

  .closing { position: absolute; left: 397px; top: 945px; width: 360px; text-align: right; font-size: 13px; line-height: 16px; }
  .closing .strong { color: var(--green-text); font-weight: 700; }
  .closing .call { color: var(--magenta); }

  .contact {
    position: absolute; left: 0; bottom: 0; width: 822px; height: 44px;
    background: var(--green-dark); color: var(--white);
    display: flex; align-items: center; justify-content: center; gap: 16px;
    font-weight: 700; font-size: 14px; letter-spacing: 1.5px;
  }
</style>
</head>
<body>
<main class="flyer">
  <svg class="swoosh" viewBox="0 0 822 1062" aria-hidden="true">
    <path d="M0 470 C 250 430, 520 250, 822 180 L 822 260 C 560 320, 300 500, 0 560 Z" fill="#ffffff" opacity="0.85"/>
    <path d="M0 540 C 300 500, 560 340, 822 300 L 822 1062 L 0 1062 Z" fill="#eeeeee"/>
  </svg>

  <div class="hero-photo" role="img" aria-label="Photo of a technician with a laptop working at an open server rack in a data centre"></div>

  <header class="brand">
    <div class="brand-name"><span class="brand-dot"></span>corvanta</div>
    <div class="brand-strap">YOUR LOCAL IT COMPANY</div>
  </header>

  <div class="circle circle-product"><div class="fill" role="img" aria-label="Photo of a boxed anti-virus software product"></div></div>
  <div class="circle circle-person"><div class="fill" role="img" aria-label="Photo of a smiling support engineer holding a laptop"></div></div>

  <div class="panel"></div>

  <table class="packages">
    <colgroup><col class="col-label"><col class="col-plan"><col class="col-plan"><col class="col-plan"><col class="col-plan"></colgroup>
    <thead>
      <tr><th class="title">IT SUPPORT PACKAGES</th><th>REMOTE</th><th>PLUS</th><th>PRO</th><th>UNLIMITED</th></tr>
    </thead>
    <tbody>
      <tr class="price"><td class="label">Per Server</td><td>£45pm</td><td>£85pm</td><td>£85pm</td><td>£85pm</td></tr>
      <tr class="price"><td class="label">Per Computers</td><td>£10pm</td><td>£10pm</td><td>£13pm</td><td>£15pm</td></tr>
      <tr class="section"><td colspan="5">Support service</td></tr>
      <tr><td class="label">Server support</td><td><i class="tick"></i></td><td><i class="tick"></i></td><td><i class="tick"></i></td><td><i class="tick"></i></td></tr>
      <tr><td class="label">PC/device support</td><td><i class="tick"></i></td><td><i class="tick"></i></td><td><i class="tick"></i></td><td><i class="tick"></i></td></tr>
      <tr class="section"><td colspan="5">Server/Network callout</td></tr>
      <tr><td class="label">Remote support</td><td><i class="tick"></i></td><td><i class="tick"></i></td><td><i class="tick"></i></td><td><i class="tick"></i></td></tr>
      <tr><td class="label">Onsite callout (4hr response)</td><td>£40</td><td><i class="tick"></i></td><td><i class="tick"></i></td><td><i class="tick"></i></td></tr>
      <tr><td class="label">Hourly rate onsite</td><td>£25ph</td><td class="small">Included</td><td class="small">Included</td><td class="small">Included</td></tr>
      <tr class="section"><td colspan="5">Computer/equipment/device callout</td></tr>
      <tr><td class="label">Remote support</td><td><i class="tick"></i></td><td><i class="tick"></i></td><td><i class="tick"></i></td><td><i class="tick"></i></td></tr>
      <tr><td class="label">Onsite callout (8hr response)</td><td>£40</td><td>£40</td><td><i class="tick"></i></td><td><i class="tick"></i></td></tr>
      <tr><td class="label">Hourly rate onsite</td><td>£25ph</td><td>£25ph</td><td class="small">Included</td><td class="small">Included</td></tr>
      <tr class="section"><td colspan="5">Protection/Security</td></tr>
      <tr><td class="label">Shieldra anti-virus (per PC)</td><td>£2</td><td>£2</td><td>£2</td><td><i class="tick"></i></td></tr>
      <tr><td class="label">Shieldra content filter (per PC)</td><td>£1.30</td><td>£1.30</td><td>£1.30</td><td><i class="tick"></i></td></tr>
      <tr><td class="label">Remote back-up (per unit, 5GB)</td><td>£1.50</td><td>£1.50</td><td>£1.50</td><td><i class="tick"></i></td></tr>
      <tr class="section"><td colspan="5">Monitoring</td></tr>
      <tr><td class="label">Daily back-up checks</td><td><i class="tick"></i></td><td><i class="tick"></i></td><td><i class="tick"></i></td><td><i class="tick"></i></td></tr>
      <tr><td class="label">24/7 monitoring</td><td><i class="tick"></i></td><td><i class="tick"></i></td><td><i class="tick"></i></td><td><i class="tick"></i></td></tr>
      <tr class="section"><td colspan="5">Maintenance</td></tr>
      <tr><td class="label">Patch management</td><td><i class="tick"></i></td><td><i class="tick"></i></td><td><i class="tick"></i></td><td><i class="tick"></i></td></tr>
      <tr><td class="label">Software updates</td><td><i class="tick"></i></td><td><i class="tick"></i></td><td><i class="tick"></i></td><td><i class="tick"></i></td></tr>
      <tr><td class="label">Security updates</td><td><i class="tick"></i></td><td><i class="tick"></i></td><td><i class="tick"></i></td><td><i class="tick"></i></td></tr>
    </tbody>
  </table>

  <section class="headline">
    <h1 class="headline-main">AFFORDABLE</h1>
    <h2 class="headline-sub">IT SUPPORT <span>PACKAGES</span></h2>
    <p class="headline-tag">Peace of mind for your business at competitive prices</p>
  </section>

  <div class="offer-band">
    <div class="offer-left"><b>IT</b> SUPPORT<br>FROM <b>£10PM</b></div>
    <div class="offer-right">FROM A <b>TRUSTED</b> PROVIDER<br>BASED IN <b>WREXHAM</b></div>
  </div>

  <section class="features">
    <div class="feature" style="left:0;top:0">
      <svg width="22" height="28" viewBox="0 0 22 28"><path d="M11 1a10 10 0 0 0-10 10c0 7 10 16 10 16s10-9 10-16A10 10 0 0 0 11 1z" fill="#4f8a1c"/><path d="M11 5l1.8 3.8 4 .5-3 2.8.8 4-3.6-2-3.6 2 .8-4-3-2.8 4-.5z" fill="#fff"/></svg>
      <div><b>Affordable,</b><br>local service</div>
    </div>
    <div class="feature" style="left:140px;top:0">
      <svg width="18" height="26" viewBox="0 0 18 26"><path d="M1 1h16M1 25h16M3 1c0 8 12 8 12 12S3 17 3 25M15 1c0 8-12 8-12 12s12 4 12 12" fill="none" stroke="#4f8a1c" stroke-width="2.4"/></svg>
      <div><b>4 hour</b><br>callout</div>
    </div>
    <div class="feature" style="left:250px;top:0">
      <svg width="26" height="26" viewBox="0 0 26 26"><path d="M4 8a14 14 0 0 0 14 14z" fill="#4f8a1c"/><path d="M11 15l8-8M17 5l4 4" stroke="#4f8a1c" stroke-width="2.4"/><path d="M8 20l-4 5h10z" fill="#4f8a1c"/></svg>
      <div><b>Remote</b><br>support</div>
    </div>
    <div class="feature" style="left:25px;top:48px">
      <svg width="28" height="24" viewBox="0 0 28 24"><rect x="1" y="1" width="16" height="11" rx="2" fill="#4f8a1c"/><path d="M4 12v5l5-5z" fill="#4f8a1c"/><rect x="10" y="8" width="16" height="10" rx="2" fill="#4f8a1c" stroke="#f4f4f4" stroke-width="1.5"/><path d="M23 18v5l-5-5z" fill="#4f8a1c"/></svg>
      <div><b>24/7</b><br>monitoring</div>
    </div>
    <div class="feature" style="left:170px;top:48px">
      <svg width="28" height="26" viewBox="0 0 28 26"><rect x="1.5" y="1.5" width="25" height="17" rx="1" fill="none" stroke="#4f8a1c" stroke-width="2.4"/><path d="M10 24h8M14 19v5" stroke="#4f8a1c" stroke-width="2.4"/></svg>
      <div>Server/PC builds<br><b>from £250</b></div>
    </div>
  </section>

  <p class="closing"><span class="strong">Protect your business and keep downtime costs at bay</span><br><span class="call">Call, email or live chat with us on our website today!</span></p>

  <footer class="contact">
    <span>01632 960 418</span><span>|</span><span>info@corvanta.co.uk</span><span>|</span><span>www.corvanta.co.uk</span>
  </footer>
</main>
</body>
</html>
```